House-share and Room Rental Website (With Focus on the Bedroom Landing Page)

Looking for website design for our House-share (executive accommodation) and room rental business.

Our company name is: Lodvenra could also be written as LodVenra or lodvenra. Either is fine .. just looking for a nice clean catchy logo to go with the design.

EXAMPLES
These are examples of other websites in this field that are doing well. this is a kind of baseline.
https://kelbrin.com.au/
https://www.tuvaplex.com/
https://www.nestorvi.com/
https://www.quillsa.net/
https://www.pendlebarrow.com.au/

Our business model is to rent rooms to people looking for high-quality accommodation. We fill the gap between those looking to rent rooms and those with rooms to rent. However, our model is slightly different from those already on the market as we looking to fill a massive gap in the market delivering upmarket rooms for rent.(Executive Accommodation) also in the back end will be coupled with a self management process in the back end.

We offer executive style accommodation that stands out above the rest. With special extras like fire safety.. and management processes that create happier homes. We are looking for a web design package that can help us grow and scale our business. We need a design that is captivating

Our MAIN focus is having a room landing page that stands out from the rest... The core of our business will rely on the promotion of the rooms in a share house... so the whole design relies on the BEDROOM landing page to drive results.

Target Market(s)

We have 2 markets we are aiming at ... the first market is people offering rooms to rent who want the highest rental return. The second market is people looking to rent safe, high-quality rooms, in houses that are well managed and looked after.

Industry/Entity Type

Share Economy

Logo Text

LodVenra

Number of Pages Required

5+ page

Font styles to use
Sans Serif

Colors
3276b5

Requirements
Must have
• A messaging system whereby we can create direct communication between those offering rooms and those looking for rooms.
• A call to action that says " Schedule an Inspection"
• Landing page for promoting rooms
• A home page for showing stock.
• Profile page for those selling rooms
• Profile page for those looking for rooms.
• A scheduling calendar for booking inspections
Nice to have
• Pages where new residents can lock in a room.. pay bond and rents.. and sign contracts
• Notifications
• SMS capabilities in the backend.
Should not have
• No script or handwriting fonts.

```html
<!DOCTYPE html>
<html lang="en">
<head>
<meta charset="utf-8">
<title>LodVenra – We Find Your Perfect Flatmates</title>
<link rel="stylesheet" href="https://fonts.googleapis.com/css2?family=Merriweather:wght@400;700;900&family=Roboto:wght@400;500;700&display=swap">
<style>
:root{
  --blue:#3276b5;
  --blue-dark:#245d94;
  --teal:#2fa3c0;
  --ink:#2d3338;
  --text:#55606a;
  --muted:#9aa3ab;
  --line:#e2e6ea;
  --soft:#f4f6f8;
  --white:#fff;
  --gold:#f2b51d;
}
*{box-sizing:border-box;margin:0;padding:0}
html,body{width:1200px;height:4186px;overflow:hidden}
body{position:relative;background:var(--white);font-family:"Roboto",Arial,sans-serif;color:var(--text);font-size:13px}
.serif{font-family:"Merriweather",Georgia,serif}
.abs{position:absolute}
.photo{position:absolute;overflow:hidden}
.btn{display:flex;align-items:center;justify-content:center;background:var(--blue);color:var(--white);font-family:"Merriweather",Georgia,serif;font-weight:700;font-size:12px;border-radius:2px;box-shadow:0 3px 0 var(--blue-dark)}

/* hero */
.hero{left:0;top:0;width:1200px;height:656px;background:linear-gradient(180deg,#3aa9c6 0%,#3a95c2 55%,#3e8bc0 100%)}
.hero-scene{left:0;top:0;width:1200px;height:656px;background:radial-gradient(ellipse at 30% 30%,rgba(255,255,255,.18),transparent 60%),radial-gradient(ellipse at 85% 75%,rgba(255,255,255,.12),transparent 55%)}
.brand{left:170px;top:22px;display:flex;align-items:center;gap:10px;color:var(--white);font-family:"Merriweather",Georgia,serif;font-weight:700;font-size:16px;letter-spacing:1px}
.brand .mark{width:34px;height:34px;border:2px solid var(--white);border-radius:50%}
.topbar{right:168px;top:30px;display:flex;align-items:center;gap:14px;color:var(--white)}
.call{display:flex;align-items:center;gap:8px}
.call small{display:block;font-size:9px;letter-spacing:1px;opacity:.85}
.call b{font-size:15px;font-weight:700}
.socials{display:flex;gap:6px;border-left:1px solid rgba(255,255,255,.5);padding-left:14px}
.socials i{width:22px;height:22px;border:1.5px solid var(--white);border-radius:50%;display:block}
.hero-title{left:0;top:130px;width:1200px;text-align:center;color:var(--white);font-family:"Merriweather",Georgia,serif;font-weight:900;font-size:36px}
.hero-sub{left:0;top:192px;width:1200px;text-align:center;color:var(--white);font-size:18px}
.search{left:187px;top:245px;width:818px;height:126px;background:var(--white);display:flex;padding:0 0 0 40px;box-shadow:0 8px 24px rgba(0,0,0,.12)}
.field{width:138px;margin-right:10px;padding-top:32px}
.field label{display:block;font-family:"Merriweather",Georgia,serif;font-size:12px;color:var(--ink);margin-bottom:18px}
.field span{display:flex;justify-content:space-between;align-items:center;border-bottom:1px solid var(--line);padding-bottom:6px;font-size:11px;color:var(--text)}
.field span::after{content:"";width:6px;height:6px;border-right:1.5px solid var(--muted);border-bottom:1.5px solid var(--muted);transform:rotate(45deg) translateY(-3px)}
.go{margin-left:auto;width:66px;height:100%;background:var(--blue);color:var(--white);display:flex;align-items:center;justify-content:center;gap:6px;font-family:"Merriweather",Georgia,serif;font-weight:700;font-size:13px}
.hero-note{left:0;top:402px;width:1200px;text-align:center;color:var(--white);font-size:12px}
.hero-cta{left:510px;top:446px;width:174px;height:45px}
.feature{top:586px;width:274px;height:154px;background:var(--white);box-shadow:0 6px 20px rgba(0,0,0,.1);display:flex;flex-direction:column;align-items:center;justify-content:flex-end;padding-bottom:32px;gap:24px;font-family:"Merriweather",Georgia,serif;font-size:12px;color:var(--ink);letter-spacing:.5px}
.feature.active{background:var(--blue);color:var(--white)}

/* section headings */
.sec-title{left:0;width:1200px;text-align:center;font-family:"Merriweather",Georgia,serif;font-size:20px;color:var(--ink);letter-spacing:.5px}
.sec-sub{left:0;width:1200px;text-align:center;font-size:12px;color:var(--muted)}

/* cities */
.city{display:flex;align-items:flex-end;justify-content:center;padding-bottom:14px;color:var(--white);font-family:"Merriweather",Georgia,serif;font-weight:700;font-size:14px;letter-spacing:1px}
.city-ny{left:167px;top:937px;width:273px;height:207px;background:linear-gradient(160deg,#5cc0cc,#3aa0b8);border:6px solid #dff2f5;flex-direction:column;align-items:center;justify-content:center;padding:0}
.city-ny small{font-size:10px;font-weight:400;margin-top:6px}

/* newsletter */
.news{left:0;width:1200px;height:206px;background:linear-gradient(90deg,#2fa3bf 0%,#3183b6 60%,#3276b5 100%)}
.news h3{position:absolute;left:0;top:40px;width:1200px;text-align:center;color:var(--white);font-family:"Merriweather",Georgia,serif;font-size:20px;letter-spacing:.5px}
.news p{position:absolute;left:0;top:76px;width:1200px;text-align:center;color:rgba(255,255,255,.9);font-size:12px}
.news .in{position:absolute;top:122px;height:40px;background:var(--white);font-size:12px;color:var(--text);display:flex;align-items:center;padding-left:14px}
.news .sub{position:absolute;left:714px;top:122px;width:215px;height:40px;font-size:12px;gap:8px}

/* deal cards */
.tabs{left:520px;top:1824px;width:160px;display:flex;justify-content:space-between}
.deal{top:1903px;width:271px;height:463px;background:var(--white);box-shadow:0 4px 16px rgba(0,0,0,.08)}
.deal.fade{opacity:.45}
.deal .img{position:absolute;left:8px;top:8px;right:8px;height:204px}
.deal .heart{position:absolute;right:18px;top:18px}
.deal h4{position:absolute;left:12px;top:226px;right:12px;font-family:"Merriweather",Georgia,serif;font-size:12px;line-height:1.45;color:var(--ink)}
.deal .price{position:absolute;left:12px;top:268px;font-family:"Merriweather",Georgia,serif;font-weight:900;font-size:19px;color:var(--ink)}
.deal .rate{position:absolute;right:12px;top:273px;display:flex;gap:3px}
.deal .rate i{width:13px;height:13px;background:var(--teal);display:block}
.deal .rate i.off{background:#c8d6e4}
.deal .route{position:absolute;left:12px;top:300px;right:12px;display:flex;align-items:center;gap:8px;font-size:10px;color:var(--blue)}
.deal .map{position:absolute;left:12px;top:324px;width:38px;height:32px;background:linear-gradient(135deg,#d9ead8,#c5dcea)}
.deal .city-name{position:absolute;left:60px;top:336px;font-size:10px;color:var(--text)}
.deal p{position:absolute;left:12px;top:366px;right:12px;font-size:10px;line-height:1.55;color:var(--text)}
.deal .more{position:absolute;right:12px;top:414px;width:98px;height:32px;font-size:11px}
.dots{left:0;width:1200px;display:flex;justify-content:center;gap:4px}
.dots i{width:8px;height:8px;border:1px solid var(--muted);border-radius:50%;display:block}
.dots i.on{background:var(--muted)}

/* rentals */
.rentals-bg{left:0;top:2503px;width:1200px;height:700px;background:var(--soft)}
.rent{top:2684px;width:273px;height:399px;background:var(--white);box-shadow:0 4px 16px rgba(0,0,0,.07)}
.rent .img{position:absolute;left:0;top:0;right:0;height:167px}
.rent .hearts{position:absolute;right:12px;top:12px;display:flex;gap:8px}
.rent h4{position:absolute;left:12px;top:184px;right:8px;font-family:"Merriweather",Georgia,serif;font-size:11.5px;color:var(--ink)}
.rent .cols{position:absolute;left:0;top:222px;right:0;display:flex;border-top:1px solid var(--line);border-bottom:1px solid var(--line);height:56px}
.rent .cols div{flex:1;padding:8px 12px}
.rent .cols div+div{border-left:1px solid var(--line)}
.rent small{display:block;font-size:9px;color:var(--muted)}
.rent .cols b{font-family:"Merriweather",Georgia,serif;font-size:15px;color:var(--ink)}
.rent .down{display:flex;align-items:center;gap:6px;margin-top:2px}
.rent .down i{width:16px;height:16px;border-radius:50%;background:var(--blue);display:block}
.rent .facts{position:absolute;left:12px;top:298px;right:12px;display:flex;justify-content:space-between;font-size:10px;color:var(--text)}
.rent .facts span{display:flex;align-items:center;gap:6px}
.rent .view{position:absolute;left:12px;right:12px;top:336px;height:38px;font-size:12px}

/* testimonials */
.quote{top:3585px;height:103px;background:var(--white);border:1px solid var(--line);box-shadow:0 4px 14px rgba(0,0,0,.06);padding:18px 22px;font-size:12px;line-height:1.6;color:var(--text)}
.quote::after{content:"";position:absolute;left:40px;bottom:-9px;width:16px;height:16px;background:var(--white);border-right:1px solid var(--line);border-bottom:1px solid var(--line);transform:rotate(45deg)}
.person{top:3710px;display:flex;align-items:center;gap:14px}
.avatar{width:54px;height:54px;border-radius:50%}
.person b{display:block;font-family:"Merriweather",Georgia,serif;font-size:12px;color:var(--ink);margin-bottom:4px}
.stars{color:var(--gold);font-size:11px;letter-spacing:1px}

/* footer */
.footer{left:0;top:3900px;width:1200px;height:286px;background:linear-gradient(90deg,#2a8fb5,#3276b5)}
.footer *{color:var(--white)}
.f-brand{position:absolute;left:172px;top:50px;display:flex;flex-direction:column;gap:12px;font-family:"Merriweather",Georgia,serif;font-weight:700;font-size:15px;letter-spacing:1px}
.f-brand .row{display:flex;align-items:center;gap:10px}
.f-brand .mark{width:30px;height:30px;border:2px solid var(--white);border-radius:50%}
.f-brand .soc{display:flex;gap:6px}
.f-brand .soc i{width:20px;height:20px;border:1.5px solid var(--white);border-radius:50%;display:block}
.f-col{position:absolute;top:54px}
.f-col h5{font-family:"Merriweather",Georgia,serif;font-size:13px;margin-bottom:16px}
.f-col p,.f-col li{font-size:11px;line-height:1.75;list-style:none;opacity:.92}
.f-col li.ci{display:flex;align-items:center;gap:8px}
.f-copy{position:absolute;left:0;top:240px;width:1200px;text-align:center;font-size:11px;border-top:1px solid rgba(255,255,255,.25);padding-top:12px;margin-top:-14px}
</style>
</head>
<body>

<!-- HERO -->
<section class="abs hero">
  <div class="abs hero-scene" role="img" aria-label="Bright modern living room interior tinted in teal blue"></div>
  <div class="abs brand"><span class="mark"></span>LODVENRA</div>
  <div class="abs topbar">
    <div class="call">
      <svg width="18" height="18" viewBox="0 0 24 24" fill="none" stroke="#fff" stroke-width="2"><path d="M5 3h4l2 5-3 2a12 12 0 0 0 6 6l2-3 5 2v4a2 2 0 0 1-2 2A17 17 0 0 1 3 5a2 2 0 0 1 2-2z"/></svg>
      <div><small>CALL NOW</small><b>+1-555-014-0133</b></div>
    </div>
    <div class="socials"><i></i><i></i><i></i></div>
  </div>
  <h1 class="abs hero-title">We Find Your Perfect Flatmates</h1>
  <div class="abs hero-sub">Your Search by Area</div>

  <form class="abs search">
    <div class="field"><label>Gender Preference:</label><span>Male</span></div>
    <div class="field"><label>Bathroom:</label><span>Shared</span></div>
    <div class="field"><label>Parking:</label><span>Street</span></div>
    <div class="field"><label>Type of Housemates:</label><span>Professionals</span></div>
    <div class="field"><label>Room Type:</label><span>Private</span></div>
    <div class="go">Go
      <svg width="12" height="12" viewBox="0 0 12 12" fill="none" stroke="#fff" stroke-width="1.6"><path d="M2 6h8M7 3l3 3-3 3"/></svg>
    </div>
  </form>

  <p class="abs hero-note">Advertise your room to indicate or find housemates with similar interests.</p>
  <div class="abs btn hero-cta">Schedule an Inspection</div>
</section>

<div class="abs feature" style="left:167px">
  <svg width="48" height="34" viewBox="0 0 48 34" fill="none" stroke="#2d3338" stroke-width="1.6"><path d="M3 4v26M45 18v12M3 24h42M3 18h42"/><rect x="8" y="10" width="10" height="8" rx="2"/></svg>
  FIND YOUR ROOM
</div>
<div class="abs feature active" style="left:463px">
  <svg width="48" height="40" viewBox="0 0 48 40" fill="none" stroke="#fff" stroke-width="1.6"><circle cx="20" cy="12" r="7"/><path d="M6 36c0-8 6-13 14-13s14 5 14 13"/><circle cx="33" cy="10" r="5"/><path d="M36 21c5 1 9 5 9 12"/></svg>
  MEET THE FLATMATES
</div>
<div class="abs feature" style="left:759px">
  <svg width="44" height="40" viewBox="0 0 44 40" fill="none" stroke="#2d3338" stroke-width="1.6"><ellipse cx="22" cy="17" rx="18" ry="13"/><path d="M12 28l-4 9 10-6"/><circle cx="15" cy="17" r="1.5"/><circle cx="22" cy="17" r="1.5"/><circle cx="29" cy="17" r="1.5"/></svg>
  WE'RE HERE TO HELP
</div>

<!-- CITIES -->
<h2 class="abs sec-title" style="top:822px">SEARCH LISTINGS IN TOP CITIES</h2>
<p class="abs sec-sub" style="top:857px">Proin condimentum leo nibh, at lacinia eros tempor vitae.</p>

<div class="photo city city-ny">
  <svg width="34" height="34" viewBox="0 0 34 34" fill="none" stroke="#fff" stroke-width="2.4"><circle cx="20" cy="13" r="9"/><path d="M13 20L4 30"/></svg>
  <div style="margin-top:8px">NEW YORK</div><small>LISTINGS</small>
</div>
<div class="photo city" style="left:460px;top:929px;width:280px;height:265px;background:linear-gradient(180deg,#e7c9d9 0%,#d7b5cd 45%,#7f8fa8 100%)" role="img" aria-label="Paris skyline with tower at dusk">PARIS</div>
<div class="photo city" style="left:753px;top:929px;width:279px;height:187px;background:linear-gradient(180deg,#4c86b8 0%,#2c5f8e 60%,#23405f 100%)" role="img" aria-label="London bridge over the river at evening">LONDON</div>
<div class="photo city" style="left:167px;top:1166px;width:279px;height:224px;background:linear-gradient(180deg,#6fa5d6 0%,#3d78b5 55%,#2c4f78 100%)" role="img" aria-label="Singapore waterfront skyline">SINGAPORE</div>
<div class="photo city" style="left:460px;top:1200px;width:280px;height:190px;background:linear-gradient(180deg,#3a7fd0 0%,#8e7a4a 60%,#6b5226 100%)" role="img" aria-label="Berlin ornate building under blue sky">BERLIN</div>
<div class="photo city" style="left:753px;top:1130px;width:279px;height:260px;background:linear-gradient(180deg,#9fb7cf 0%,#6f8aa6 55%,#3d5068 100%)" role="img" aria-label="Tokyo city skyline with tall tower">TOKYO</div>

<!-- NEWSLETTER 1 -->
<section class="abs news" style="top:1465px">
  <h3>SUBSCRIBE TO OUR NEWSLETTER</h3>
  <p>Nam tristique iaculis lacus, ac lobortis dui finibus vitae.</p>
  <div class="in" style="left:265px;width:209px">Your Name:</div>
  <div class="in" style="left:488px;width:210px">Email:</div>
  <div class="btn sub">Subscribe Now
    <svg width="12" height="12" viewBox="0 0 12 12" fill="#fff"><path d="M1 6l10-5-3 10-2-4z"/></svg>
  </div>
</section>

<!-- BEST SELLERS -->
<h2 class="abs sec-title" style="top:1743px">BEST SELLERS &amp; HOT DEALS</h2>
<p class="abs sec-sub" style="top:1778px">Lorem ipsum dolor sit amet, consectetur adipiscing elit. Quisque nec est ligula.</p>
<div class="abs tabs">
  <svg width="18" height="16" viewBox="0 0 18 16" fill="none" stroke="#55606a" stroke-width="1.4"><rect x="2" y="2" width="14" height="10" rx="2"/><circle cx="5" cy="14" r="1.2"/><circle cx="13" cy="14" r="1.2"/></svg>
  <svg width="20" height="16" viewBox="0 0 20 16" fill="none" stroke="#55606a" stroke-width="1.4"><path d="M2 11l2-6h12l2 6z"/><circle cx="6" cy="13" r="1.5"/><circle cx="14" cy="13" r="1.5"/></svg>
  <svg width="22" height="16" viewBox="0 0 22 16" fill="none" stroke="#55606a" stroke-width="1.4"><rect x="1" y="4" width="20" height="8" rx="2"/><circle cx="6" cy="13" r="1.5"/><circle cx="16" cy="13" r="1.5"/></svg>
  <svg width="20" height="16" viewBox="0 0 20 16" fill="none" stroke="#55606a" stroke-width="1.4"><circle cx="5" cy="11" r="3"/><circle cx="15" cy="11" r="3"/><path d="M5 11l4-6h4l2 6"/></svg>
</div>

<article class="abs deal fade" style="left:-140px">
  <div class="img" style="background:linear-gradient(135deg,#e9e4dc,#cbb9a2)" role="img" aria-label="Bright living room with wooden floor"></div>
  <h4>Etiam finibus sem est, at porta velit</h4>
  <div class="price">$420</div>
  <div class="route">Gregory Lane</div>
  <p>Morbi maximus a enim quam ut sodales.</p>
  <div class="btn more">Read More</div>
</article>

<article class="abs deal" style="left:167px">
  <div class="img" style="background:linear-gradient(135deg,#c7c9cc,#7d8185)" role="img" aria-label="Grey lounge with sofa and wall unit"></div>
  <h4>Phasellus convallis erat diam, eu pellentesque.</h4>
  <div class="price">$500</div>
  <div class="rate"><i></i><i></i><i></i><i></i><i class="off"></i><i class="off"></i><i class="off"></i></div>
  <div class="route"><span>Monterey</span><svg width="30" height="8" viewBox="0 0 30 8" fill="none" stroke="#3276b5" stroke-width="1.2"><path d="M0 4h28M25 1l3 3-3 3"/></svg><span>Pine Street</span></div>
  <div class="map" role="img" aria-label="Small location map"></div>
  <div class="city-name">City Monterey</div>
  <p>Etiam id porttitor lorem. Morbi maximus a enim quam ut sodales. Proin tincidunt metus a convallis fringilla.</p>
  <div class="btn more">Read More</div>
</article>

<article class="abs deal" style="left:463px">
  <div class="img" style="background:linear-gradient(135deg,#e6d7c2,#a98a68)" role="img" aria-label="Warm lit living room with armchairs"></div>
  <svg class="heart" width="16" height="14" viewBox="0 0 16 14" fill="none" stroke="#fff" stroke-width="1.5"><path d="M8 13S1 8.5 1 4.5A3.5 3.5 0 0 1 8 3a3.5 3.5 0 0 1 7 1.5C15 8.5 8 13 8 13z"/></svg>
  <h4>Etiam finibus sem est, at porta velit cursus vel.</h4>
  <div class="price">$530</div>
  <div class="rate"><i></i><i></i><i></i><i></i><i class="off"></i><i class="off"></i><i class="off"></i></div>
  <div class="route"><span>Kentucky</span><svg width="30" height="8" viewBox="0 0 30 8" fill="none" stroke="#3276b5" stroke-width="1.2"><path d="M0 4h28M25 1l3 3-3 3"/></svg><span>1077 Alder Lane</span></div>
  <div class="map" role="img" aria-label="Small location map"></div>
  <div class="city-name">City Louisville</div>
  <p>Etiam id porttitor lorem. Morbi maximus a enim quam ut sodales. Proin tincidunt metus a convallis fringilla.</p>
  <div class="btn more">Read More</div>
</article>

<article class="abs deal" style="left:759px">
  <div class="img" style="background:linear-gradient(135deg,#b7c6d6,#4f6784)" role="img" aria-label="Blue toned lounge with sectional sofa"></div>
  <svg class="heart" width="16" height="14" viewBox="0 0 16 14" fill="none" stroke="#fff" stroke-width="1.5"><path d="M8 13S1 8.5 1 4.5A3.5 3.5 0 0 1 8 3a3.5 3.5 0 0 1 7 1.5C15 8.5 8 13 8 13z"/></svg>
  <h4>Praesent sed fringilla justo. In posuere tellus.</h4>
  <div class="price">$600</div>
  <div class="rate"><i></i><i></i><i></i><i></i><i class="off"></i><i class="off"></i><i class="off"></i></div>
  <div class="route"><span>Douglas</span><svg width="30" height="8" viewBox="0 0 30 8" fill="none" stroke="#3276b5" stroke-width="1.2"><path d="M0 4h28M25 1l3 3-3 3"/></svg><span>Volunteer Drive</span></div>
  <div class="map" role="img" aria-label="Small location map"></div>
  <div class="city-name">City Douglas</div>
  <p>Etiam id porttitor lorem. Morbi maximus a enim quam ut sodales. Proin tincidunt metus a convallis fringilla.</p>
  <div class="btn more">Read More</div>
</article>

<article class="abs deal fade" style="left:1052px">
  <div class="img" style="background:linear-gradient(135deg,#e4e8ec,#b2bcc6)" role="img" aria-label="White open plan living room"></div>
  <h4>Etiam finibus sem est, at porta velit</h4>
  <div class="price">$520</div>
  <div class="route">Kentucky</div>
  <p>Morbi maximus a enim quam ut sodales.</p>
  <div class="btn more">Read More</div>
</article>

<div class="abs dots" style="top:2407px"><i class="on"></i><i></i><i></i><i></i></div>

<!-- POPULAR RENTALS -->
<div class="abs rentals-bg"></div>
<h2 class="abs sec-title" style="top:2574px">POPULAR RENTALS</h2>
<p class="abs sec-sub" style="top:2610px">Phasellus sollicitudin neque nec ipsum aliquam elementum.</p>

<article class="abs rent" style="left:167px">
  <div class="img" style="background:linear-gradient(135deg,#ecebe6,#b9b2a4)" role="img" aria-label="Living room with white sofa and rug"></div>
  <div class="hearts">
    <svg width="14" height="12" viewBox="0 0 16 14" fill="none" stroke="#fff" stroke-width="1.5"><path d="M8 13S1 8.5 1 4.5A3.5 3.5 0 0 1 8 3a3.5 3.5 0 0 1 7 1.5C15 8.5 8 13 8 13z"/></svg>
    <svg width="14" height="12" viewBox="0 0 16 14" fill="none" stroke="#fff" stroke-width="1.5"><path d="M2 7h12M10 3l4 4-4 4"/></svg>
  </div>
  <h4>702 Linden Ave N, Fairholt MN 55075</h4>
  <div class="cols"><div><small>For Sale</small><b>$249,900</b></div><div><small>Market value down</small><span class="down"><i></i><b>15%</b></span></div></div>
  <div class="facts"><span>▭ 4 Beds</span><span>◫ 3 Baths</span><span>⌗ 1,860 sqft</span></div>
  <div class="btn view">View Details</div>
</article>

<article class="abs rent" style="left:463px">
  <div class="img" style="background:linear-gradient(135deg,#f0ede8,#a9a59c)" role="img" aria-label="Bright lounge with grey sofa"></div>
  <div class="hearts">
    <svg width="14" height="12" viewBox="0 0 16 14" fill="none" stroke="#fff" stroke-width="1.5"><path d="M8 13S1 8.5 1 4.5A3.5 3.5 0 0 1 8 3a3.5 3.5 0 0 1 7 1.5C15 8.5 8 13 8 13z"/></svg>
    <svg width="14" height="12" viewBox="0 0 16 14" fill="none" stroke="#fff" stroke-width="1.5"><path d="M2 7h12M10 3l4 4-4 4"/></svg>
  </div>
  <h4>807 Linden Ave N, Fairholt MN 55078</h4>
  <div class="cols"><div><small>For Sale</small><b>$240,100</b></div><div><small>Market value down</small><span class="down"><i></i><b>15%</b></span></div></div>
  <div class="facts"><span>▭ 4 Beds</span><span>◫ 3 Baths</span><span>⌗ 1,860 sqft</span></div>
  <div class="btn view">View Details</div>
</article>

<article class="abs rent" style="left:759px">
  <div class="img" style="background:linear-gradient(135deg,#e2d6c8,#8f7a66)" role="img" aria-label="Living room with beige sofa and wood floor"></div>
  <div class="hearts">
    <svg width="14" height="12" viewBox="0 0 16 14" fill="none" stroke="#fff" stroke-width="1.5"><path d="M8 13S1 8.5 1 4.5A3.5 3.5 0 0 1 8 3a3.5 3.5 0 0 1 7 1.5C15 8.5 8 13 8 13z"/></svg>
    <svg width="14" height="12" viewBox="0 0 16 14" fill="none" stroke="#fff" stroke-width="1.5"><path d="M2 7h12M10 3l4 4-4 4"/></svg>
  </div>
  <h4>702 Birch Ave N, Fairholt MN 55065</h4>
  <div class="cols"><div><small>For Sale</small><b>$239,900</b></div><div><small>Market value down</small><span class="down"><i style="background:var(--teal)"></i><b>15%</b></span></div></div>
  <div class="facts"><span>▭ 4 Beds</span><span>◫ 3 Baths</span><span>⌗ 1,860 sqft</span></div>
  <div class="btn view">View Details</div>
</article>

<div class="abs dots" style="top:3121px"><i class="on"></i><i></i><i></i><i></i></div>

<!-- NEWSLETTER 2 -->
<section class="abs news" style="top:3203px">
  <h3>SUBSCRIBE TO OUR NEWSLETTER</h3>
  <p>Nam tristique iaculis lacus, ac lobortis dui finibus vitae.</p>
  <div class="in" style="left:265px;width:209px">Your Name:</div>
  <div class="in" style="left:488px;width:210px">Email:</div>
  <div class="btn sub">Subscribe Now
    <svg width="12" height="12" viewBox="0 0 12 12" fill="#fff"><path d="M1 6l10-5-3 10-2-4z"/></svg>
  </div>
</section>

<!-- TESTIMONIALS -->
<h2 class="abs sec-title" style="top:3478px">OUR TESTIMONIALS</h2>
<p class="abs sec-sub" style="top:3513px">Nunc eget arcu cursus, placerat velit consequat, lobortis sapien.</p>

<blockquote class="abs quote" style="left:201px;width:371px">Fusce ornare a nisl a efficitur. Aliquam sed metus et nunc tempor convallis. Suspendisse auctor eros et ante suscipit, et sagittis ipsum sollicitudin.</blockquote>
<div class="abs person" style="left:201px">
  <div class="avatar" style="background:linear-gradient(135deg,#c9a88a,#6e5340)" role="img" aria-label="Reviewer portrait"></div>
  <div><b>Reid Calloway</b><span class="stars">★★★★★</span></div>
</div>

<blockquote class="abs quote" style="left:619px;width:377px">Duis faucibus quam ac pretium fringilla. Quisque eget justo quis lectus laoreet placerat. Nullam convallis libero ac dui convallis malesuada.</blockquote>
<div class="abs person" style="left:619px">
  <div class="avatar" style="background:linear-gradient(135deg,#d6d6d6,#5a5a5a)" role="img" aria-label="Reviewer portrait"></div>
  <div><b>Miles Varden</b><span class="stars">★★★★★</span></div>
</div>

<!-- FOOTER -->
<footer class="abs footer">
  <div class="f-brand">
    <div class="row"><span class="mark"></span>LODVENRA</div>
    <div class="soc"><i></i><i></i><i></i></div>
  </div>
  <div class="f-col" style="left:350px;width:240px">
    <h5>About Us</h5>
    <p>Nam efficitur feugiat facilisis. Ut non placerat nisl. Ut nulla risus, bibendum ut nulla sed, placerat bibendum nisl.</p>
  </div>
  <div class="f-col" style="left:664px">
    <h5>Others</h5>
    <ul><li>Privacy</li><li>Terms of Use</li><li>Contact Us</li></ul>
  </div>
  <div class="f-col" style="left:851px">
    <h5>Contact Us</h5>
    <ul>
      <li class="ci"><svg width="10" height="12" viewBox="0 0 10 12" fill="#fff"><path d="M5 0a4 4 0 0 1 4 4c0 3-4 8-4 8S1 7 1 4a4 4 0 0 1 4-4z"/></svg>48 Marlow Court, California</li>
      <li class="ci"><svg width="10" height="10" viewBox="0 0 24 24" fill="#fff"><path d="M5 3h4l2 5-3 2a12 12 0 0 0 6 6l2-3 5 2v4a2 2 0 0 1-2 2A17 17 0 0 1 3 5a2 2 0 0 1 2-2z"/></svg>+1-555-014-0133</li>
      <li class="ci"><svg width="11" height="9" viewBox="0 0 12 9" fill="none" stroke="#fff" stroke-width="1.3"><rect x=".5" y=".5" width="11" height="8"/><path d="M.5.5l5.5 4 5.5-4"/></svg>info@lodvenra.com</li>
    </ul>
  </div>
  <div class="f-copy">©2019 Lodvenra. All Right Reserved.</div>
</footer>

</body>
</html>
```